Request for Web Design Services – Lantern Route

We are excited to announce a new project and are seeking talented web designers to create a visually stunning and intuitive website for our upcoming service, "Lantern Route." This platform is dedicated to assisting foreign visitors in planning their journeys across Japan by highlighting the nation's beautiful shrines and temples. Please refer to the attached document for detailed design requirements.

Project Overview:
-Site Name: Lantern Route
-Target Audience: Visitors to Japan
-Usage Scenario: Trip planning before and during the visit to Japan

Functionalities:
-Plotting the names and locations of shrines and temples across Japan
-Enabling users to select multiple shrines and temples and proposing optimal touring routes
-Intuitive user interface without relying heavily on language explanations

Deliverables:
-Source code (HTML, CSS, JavaScript, etc.)
-Site name logo
-Icons
-Favicon

Deadline:May 1, 2024

Design Requirements:
-Responsive design for both PC and mobile devices

Design Preferences:
-Catchy design suitable for coverage in domestic and international news media
-Unique design not typically created by Japanese designers
-Incorporation of Japanese traditions while maintaining a modern aesthetic
-Inclusion of motifs representing shrines and temples, such as bells and omikuji

We look forward to receiving your creative proposals and collaborating on this exciting project.

Best regards

Target Market(s)

Visitors to Japan

Industry/Entity Type

Information Technology

Coding

Coded - Design and coding required

Number of Pages Required

3 page

```html
<!DOCTYPE html>
<html lang="en">
<head>
<meta charset="utf-8">
<title>Lantern Route – Route Planner Screens</title>
<link rel="stylesheet" href="https://fonts.googleapis.com/css2?family=Roboto:wght@400;500;700&family=Noto+Sans+JP:wght@400;500&family=Yellowtail&display=swap">
<style>
:root{
  --page:#f4f4f4;
  --frame:#ffffff;
  --ink:#1f1d1b;
  --ink-soft:#55514c;
  --red:#f0483e;
  --orange:#e8762c;
  --line:#d9d6d2;
  --map-light:#cdc7b9;
  --map-mid:#b3ab9a;
  --map-deep:#8f8672;
  --dim:rgba(28,26,24,.58);
}
*{box-sizing:border-box;margin:0;padding:0}
html,body{width:819px;height:1200px;overflow:hidden;background:var(--page)}
body{position:relative;font-family:"Roboto","Noto Sans JP",sans-serif;color:var(--ink)}
.frame{position:absolute;background:var(--frame);transform-origin:0 0;transform:scale(.5167);box-shadow:0 2px 10px rgba(0,0,0,.12);border-radius:6px}
.frame.desktop{width:956px;height:649px}
.frame.mobile{width:308px;height:649px}
.screen{position:absolute;left:7px;top:8px;width:942px;height:632px;overflow:hidden}
.mobile .screen{left:8px;width:292px}
.map{position:absolute;inset:0;background:
  radial-gradient(ellipse 38% 34% at 72% 32%,rgba(128,117,97,.6),transparent 72%),
  radial-gradient(ellipse 32% 40% at 38% 72%,rgba(134,124,104,.5),transparent 72%),
  radial-gradient(ellipse 26% 30% at 14% 22%,rgba(222,218,208,.7),transparent 72%),
  radial-gradient(ellipse 28% 22% at 78% 86%,rgba(222,218,208,.6),transparent 72%),
  radial-gradient(ellipse 22% 26% at 52% 12%,rgba(214,209,198,.6),transparent 72%),
  linear-gradient(160deg,var(--map-light),var(--map-mid) 50%,var(--map-light))}
.pin{position:absolute;width:40px;height:52px}
.mobile .pin{width:36px;height:46px}
.pin-num{position:absolute;width:22px;height:22px;border-radius:50%;background:var(--ink);color:#fff;font:700 12px/18px "Roboto",sans-serif;text-align:center;border:2px solid #fff}
.mobile .pin-num{width:16px;height:16px;font-size:9px;line-height:12px}
.pin-num.active{background:var(--red)}
.logo-bar{position:absolute;background:#fff;border-radius:26px;display:flex;align-items:center;box-shadow:0 2px 6px rgba(0,0,0,.15)}
.logo-mark{border-radius:50%;background:var(--red);flex:none}
.logo-name{font-weight:500;color:var(--ink);white-space:nowrap}
.search-btn{margin-left:auto;border-radius:50%;background:var(--red);display:flex;align-items:center;justify-content:center;flex:none}
.pill{position:absolute;border-radius:20px;color:#fff;font-weight:700;display:flex;align-items:center;justify-content:center;gap:6px;text-align:center;line-height:1.1}
.pill.red{background:var(--red)}
.pill.orange{background:var(--orange)}
.pill .dot{width:7px;height:7px;border-radius:50%;background:#fff}
.panel{position:absolute;left:10px;top:74px;width:246px;height:490px;background:#fff;border-radius:14px;box-shadow:0 2px 8px rgba(0,0,0,.15)}
.panel-head{position:absolute;left:3px;top:5px;width:242px;height:37px;background:var(--ink);border-radius:6px;color:#fff;font:500 14px/37px "Roboto",sans-serif;padding-left:15px}
.panel-head svg{position:absolute;right:10px;top:15px}
.share{position:absolute;left:159px;top:63px;width:70px;height:27px;border:1px solid var(--red);border-radius:14px;font-size:9px;font-weight:500;display:flex;align-items:center;justify-content:center;gap:4px}
.stop{position:absolute;left:53px;width:177px;height:33px;border:1px solid var(--line);border-radius:3px;font-size:8.5px;line-height:11px;padding:5px 9px;background:#fff}
.stop.current{background:var(--red);border-color:var(--red);color:#fff}
.stop .more{position:absolute;right:10px;top:9px;width:2px;height:10px;background:radial-gradient(circle,currentColor 1px,transparent 1.2px) 0 0/2px 4px}
.stop-num{position:absolute;left:17px;width:16px;height:16px;border-radius:50%;background:var(--ink);color:#fff;font-size:8px;font-weight:700;line-height:16px;text-align:center;box-shadow:0 0 0 3px #fff,0 0 0 4px var(--line)}
.stop-num.current{background:var(--red)}
.stop-link{position:absolute;left:141px;width:1px;height:21px;background:var(--line)}
.stop-meta{position:absolute;left:110px;top:150px;font-size:6.5px;color:var(--ink-soft)}
.optimize{position:absolute;left:13px;top:440px;width:216px;height:36px;border:1.5px solid var(--red);border-radius:18px;font:500 11px/33px "Roboto",sans-serif;text-align:center}
.scroll{position:absolute;left:243px;top:76px;width:2px;height:90px;background:#bbb;border-radius:1px}
.filter-bar{position:absolute;background:#fff;border-radius:6px;box-shadow:0 2px 6px rgba(0,0,0,.15)}
.filter-select{position:absolute;border:1px solid var(--line);border-radius:3px;display:flex;align-items:center;justify-content:space-between;padding:0 10px}
.filter-select::after{content:"";border-left:5px solid var(--ink);border-top:4px solid transparent;border-bottom:4px solid transparent}
.track{position:absolute;height:3px;background:#cfcac4;border-radius:2px}
.track .range{position:absolute;top:0;height:3px;background:var(--red)}
.knob{position:absolute;top:-6px;width:14px;height:14px;border-radius:50%;background:#fff;border:3px solid var(--red)}
.zoom{position:absolute;background:#fff;border-radius:3px;box-shadow:0 1px 4px rgba(0,0,0,.2);display:flex;flex-direction:column;align-items:center;justify-content:space-around;font-weight:700;color:var(--ink)}
.callout{position:absolute;background:#fff;border-radius:3px;box-shadow:0 2px 6px rgba(0,0,0,.2);color:var(--ink)}
.badge{position:absolute;border-radius:50%;background:var(--red);color:#fff;font-weight:700;text-align:center;border:2px solid #fff}
.info-card{position:absolute;background:#fff;border-radius:4px;box-shadow:0 2px 8px rgba(0,0,0,.2)}
.info-card h3{font-weight:500;letter-spacing:1px}
.info-card .close{position:absolute;border-radius:50%;background:var(--red)}
.btn-fill{background:var(--red);color:#fff;border-radius:14px;text-align:center}
.btn-line{border:1px solid var(--red);border-radius:14px;text-align:center}
.footer{position:absolute;left:0;right:0;bottom:0;background:var(--ink);color:#fff;text-align:center}
.footer b{font-weight:700}
.desktop .footer{height:45px;font-size:11px;line-height:45px}
.desktop .footer .code{position:absolute;right:45px;top:0;font-size:9px}
.mobile .footer{height:36px;font-size:7px;line-height:12px;padding-top:6px}
.dim{position:absolute;inset:0;background:var(--dim)}
.modal{position:absolute;background:#fff;border-radius:16px;box-shadow:0 4px 20px rgba(0,0,0,.35);text-align:center}
.modal .close{position:absolute;border-radius:50%;background:var(--red)}
.modal-title{font-family:"Yellowtail","Brush Script MT",cursive;color:var(--ink);font-weight:400}
.modal-title em{font-style:normal;color:#e9a29d}
.japan{position:absolute;background:linear-gradient(160deg,#f2f0ee,#e6e2de);border-radius:8px}
.region{position:absolute;background:#fff;border:1.5px solid var(--red);border-radius:12px;font-weight:500;color:var(--ink);padding:0 10px;white-space:nowrap}
.region.hub{background:var(--orange);border-color:var(--orange);color:#fff}
.modal hr{position:absolute;border:0;border-top:1px solid var(--line)}
.airports{position:absolute;left:0;right:0;display:flex;flex-direction:column;align-items:center}
.airport-row{display:flex;justify-content:center}
.airport{display:flex;align-items:center;border:1.5px solid var(--red);border-radius:14px;font-weight:500;color:var(--ink);white-space:nowrap}
.airport i{border-radius:50%;background:var(--red);display:flex;align-items:center;justify-content:center;flex:none}
</style>
</head>
<body>

<svg width="0" height="0" style="position:absolute" aria-hidden="true">
  <defs>
    <symbol id="pin-dark" viewBox="0 0 40 52">
      <path d="M20 2a18 18 0 0 1 18 18c0 13-18 30-18 30S2 33 2 20A18 18 0 0 1 20 2z" fill="#1f1d1b" stroke="#fff" stroke-width="2.5"/>
      <circle cx="20" cy="20" r="11" fill="#fff"/>
      <text x="20" y="23" text-anchor="middle" font-family="Roboto,sans-serif" font-size="8" font-weight="700" fill="#1f1d1b">360</text>
    </symbol>
    <symbol id="pin-red" viewBox="0 0 40 52">
      <path d="M20 2a18 18 0 0 1 18 18c0 13-18 30-18 30S2 33 2 20A18 18 0 0 1 20 2z" fill="#f0483e" stroke="#fff" stroke-width="2.5"/>
      <circle cx="20" cy="20" r="11" fill="#fff"/>
      <text x="20" y="23" text-anchor="middle" font-family="Roboto,sans-serif" font-size="8" font-weight="700" fill="#f0483e">360</text>
    </symbol>
    <symbol id="ico-search" viewBox="0 0 16 16"><circle cx="7" cy="7" r="4.5" fill="none" stroke="#fff" stroke-width="2"/><path d="M10.5 10.5l3.5 3.5" stroke="#fff" stroke-width="2"/></symbol>
    <symbol id="ico-share" viewBox="0 0 12 12"><circle cx="3" cy="6" r="2" fill="#1f1d1b"/><circle cx="9" cy="2.5" r="2" fill="#1f1d1b"/><circle cx="9" cy="9.5" r="2" fill="#1f1d1b"/><path d="M3 6L9 2.5M3 6l6 3.5" stroke="#1f1d1b" stroke-width="1.2"/></symbol>
    <symbol id="ico-plane" viewBox="0 0 12 12"><path d="M2 10l8-8M5 3l5-1-1 5M4 8l-1 3" stroke="#fff" stroke-width="1.6" fill="none" stroke-linecap="round"/></symbol>
    <symbol id="ico-close" viewBox="0 0 12 12"><path d="M4 4l4 4M8 4l-4 4" stroke="#fff" stroke-width="1.5"/></symbol>
  </defs>
</svg>

<!-- ============ Row 1 · desktop: route selected ============ -->
<section class="frame desktop" style="left:62px;top:56px">
  <div class="screen">
    <div class="map" role="img" aria-label="Terrain map of the mountain region around Kofu with roads, peaks and place names"></div>
    <svg class="pin" style="left:456px;top:29px"><use href="#pin-dark"/></svg>
    <svg class="pin" style="left:736px;top:54px"><use href="#pin-dark"/></svg>
    <svg class="pin" style="left:623px;top:127px"><use href="#pin-dark"/></svg>
    <svg class="pin" style="left:496px;top:162px"><use href="#pin-dark"/></svg>
    <svg class="pin" style="left:330px;top:201px"><use href="#pin-dark"/></svg>
    <svg class="pin" style="left:680px;top:226px"><use href="#pin-dark"/></svg>
    <svg class="pin" style="left:835px;top:184px"><use href="#pin-dark"/></svg>
    <svg class="pin" style="left:451px;top:292px"><use href="#pin-dark"/></svg>
    <svg class="pin" style="left:803px;top:347px"><use href="#pin-dark"/></svg>
    <svg class="pin" style="left:551px;top:372px"><use href="#pin-dark"/></svg>
    <svg class="pin" style="left:276px;top:381px"><use href="#pin-dark"/></svg>
    <svg class="pin" style="left:699px;top:441px"><use href="#pin-dark"/></svg>
    <svg class="pin" style="left:813px;top:484px"><use href="#pin-dark"/></svg>
    <svg class="pin" style="left:366px;top:456px"><use href="#pin-dark"/></svg>
    <svg class="pin" style="left:400px;top:327px"><use href="#pin-red"/></svg>

    <div class="callout" style="left:368px;top:384px;width:101px;height:52px;font-size:11px;line-height:16px;padding:9px 13px">地蔵寺<br>Jizo Temple</div>
    <div class="badge" style="left:442px;top:372px;width:24px;height:24px;font-size:11px;line-height:20px">1</div>
    <div class="badge" style="left:450px;top:428px;width:16px;height:16px;font-size:11px;line-height:11px">+</div>

    <div class="logo-bar" style="left:10px;top:12px;width:246px;height:52px;padding:0 6px 0 10px;gap:9px">
      <span class="logo-mark" style="width:28px;height:28px"></span>
      <span class="logo-name" style="font-size:15px">Lantern Route</span>
      <span class="search-btn" style="width:26px;height:26px"><svg width="14" height="14"><use href="#ico-search"/></svg></span>
    </div>
    <div class="pill red" style="left:273px;top:24px;width:76px;height:28px;font-size:11px">360° ON <span class="dot"></span></div>

    <div class="panel">
      <div class="panel-head">PLANNING<svg width="9" height="6"><path d="M0 0h9L4.5 6z" fill="#fff"/></svg></div>
      <div class="share"><svg width="9" height="9"><use href="#ico-share"/></svg>SHARE</div>
      <div class="scroll"></div>
      <span class="stop-num current" style="top:114px">1</span>
      <div class="stop current" style="top:106px">地蔵寺<br>Jizo Temple<span class="more"></span></div>
      <div class="stop-meta">🚗 2 km &nbsp; ◷ 10 min</div>
      <span class="stop-num" style="top:168px">2</span>
      <div class="stop" style="top:160px">地蔵寺<br>Jizo Temple<span class="more"></span></div>
      <div class="stop-link" style="top:193px"></div>
      <span class="stop-num" style="top:222px">3</span>
      <div class="stop" style="top:214px">地蔵寺<br>Jizo Temple<span class="more"></span></div>
      <div class="stop-link" style="top:247px"></div>
      <span class="stop-num" style="top:276px">4</span>
      <div class="stop" style="top:268px">地蔵寺<br>Jizo Temple<span class="more"></span></div>
      <div class="stop-link" style="top:301px"></div>
      <span class="stop-num" style="top:330px">5</span>
      <div class="stop" style="top:322px">地蔵寺<br>Jizo Temple<span class="more"></span></div>
      <div class="stop-link" style="top:355px"></div>
      <span class="stop-num" style="top:384px">6</span>
      <div class="stop" style="top:376px">地蔵寺<br>Jizo Temple<span class="more"></span></div>
      <div class="optimize">OPTIMIZE ROUTE ORDER</div>
    </div>

    <div class="filter-bar" style="left:273px;top:516px;width:525px;height:48px">
      <div class="filter-select" style="left:5px;top:5px;width:108px;height:38px;font-size:12px">Popular</div>
      <div class="track" style="left:143px;top:23px;width:359px"><span class="range" style="left:211px;width:148px"></span><span class="knob" style="left:204px"></span><span class="knob" style="left:352px"></span></div>
    </div>
    <div class="zoom" style="left:895px;top:502px;width:28px;height:64px;font-size:16px"><span>+</span><span>−</span></div>

    <div class="footer"><b>Lantern Route</b> &nbsp;|&nbsp; Confidential and Proprietary &nbsp;|&nbsp; Terms of Use &nbsp;|&nbsp; External Transmission Policy<span class="code">C45</span></div>
  </div>
</section>

<!-- ============ Row 1 · mobile ============ -->
<section class="frame mobile" style="left:598px;top:56px">
  <div class="screen">
    <div class="map" role="img" aria-label="Terrain map with roads, peaks and place names"></div>
    <svg class="pin" style="left:34px;top:224px"><use href="#pin-dark"/></svg>
    <svg class="pin" style="left:177px;top:224px"><use href="#pin-dark"/></svg>
    <svg class="pin" style="left:104px;top:316px"><use href="#pin-dark"/></svg>
    <svg class="pin" style="left:88px;top:429px"><use href="#pin-dark"/></svg>
    <svg class="pin" style="left:207px;top:376px"><use href="#pin-red"/></svg>
    <div class="callout" style="left:186px;top:424px;width:70px;height:40px;font-size:8px;line-height:12px;padding:7px 9px">地蔵寺<br>Jizo Temple</div>
    <div class="badge" style="left:244px;top:412px;width:16px;height:16px;font-size:8px;line-height:12px">1</div>
    <div class="badge" style="left:248px;top:456px;width:12px;height:12px;font-size:8px;line-height:8px">+</div>

    <div class="pill orange" style="left:14px;top:24px;width:78px;height:27px;font-size:6.5px">OPTIMIZE ROUTE<br>ORDER</div>
    <div class="logo-bar" style="left:109px;top:20px;width:102px;height:32px;padding:0 4px 0 6px;gap:5px">
      <span class="logo-mark" style="width:16px;height:16px"></span>
      <span class="logo-name" style="font-size:8px">Lantern Route</span>
      <span class="search-btn" style="width:16px;height:16px"><svg width="9" height="9"><use href="#ico-search"/></svg></span>
    </div>
    <div class="pill red" style="left:226px;top:25px;width:54px;height:24px;font-size:8px;gap:4px">360° ON <span class="dot" style="width:5px;height:5px"></span></div>

    <div class="zoom" style="left:254px;top:504px;width:20px;height:40px;font-size:11px"><span>+</span><span>−</span></div>
    <div class="filter-bar" style="left:26px;top:544px;width:240px;height:28px">
      <div class="filter-select" style="left:4px;top:4px;width:68px;height:20px;font-size:7px;padding:0 6px">Popular</div>
      <div class="track" style="left:92px;top:13px;width:135px;height:2px"><span class="range" style="left:82px;width:53px;height:2px"></span><span class="knob" style="left:78px;top:-4px;width:9px;height:9px;border-width:2px"></span><span class="knob" style="left:129px;top:-4px;width:9px;height:9px;border-width:2px"></span></div>
    </div>
    <div class="footer"><b>Lantern Route</b> &nbsp;|&nbsp; Confidential and Proprietary &nbsp;|&nbsp; Terms of Use &nbsp;|<br>External Transmission Policy</div>
  </div>
</section>

<!-- ============ Row 2 · desktop: spot detail ============ -->
<section class="frame desktop" style="left:62px;top:433px">
  <div class="screen">
    <div class="map" role="img" aria-label="Terrain map with roads, peaks and place names"></div>
    <svg class="pin" style="left:456px;top:29px"><use href="#pin-dark"/></svg>
    <svg class="pin" style="left:623px;top:127px"><use href="#pin-dark"/></svg>
    <svg class="pin" style="left:496px;top:162px"><use href="#pin-dark"/></svg>
    <span class="pin-num" style="left:505px;top:219px">2</span>
    <svg class="pin" style="left:330px;top:201px"><use href="#pin-dark"/></svg>
    <svg class="pin" style="left:680px;top:226px"><use href="#pin-dark"/></svg>
    <span class="pin-num" style="left:689px;top:283px">3</span>
    <svg class="pin" style="left:835px;top:184px"><use href="#pin-dark"/></svg>
    <svg class="pin" style="left:451px;top:292px"><use href="#pin-dark"/></svg>
    <svg class="pin" style="left:803px;top:347px"><use href="#pin-dark"/></svg>
    <span class="pin-num" style="left:812px;top:405px">4</span>
    <svg class="pin" style="left:551px;top:372px"><use href="#pin-dark"/></svg>
    <span class="pin-num" style="left:560px;top:429px">6</span>
    <svg class="pin" style="left:276px;top:381px"><use href="#pin-dark"/></svg>
    <svg class="pin" style="left:699px;top:441px"><use href="#pin-dark"/></svg>
    <span class="pin-num" style="left:708px;top:498px">5</span>
    <svg class="pin" style="left:813px;top:484px"><use href="#pin-dark"/></svg>
    <svg class="pin" style="left:366px;top:456px"><use href="#pin-dark"/></svg>
    <svg class="pin" style="left:400px;top:327px"><use href="#pin-red"/></svg>
    <span class="pin-num active" style="left:409px;top:383px">1</span>

    <div class="info-card" style="left:756px;top:12px;width:167px;height:114px;padding:10px 13px">
      <h3 style="font-size:22px">XXXXX</h3>
      <p style="font-size:10px;line-height:13px;margin-top:5px;color:var(--ink-soft)">XXXX &nbsp; XXXX<br>XXXX &nbsp; XXXX</p>
      <div style="display:flex;gap:5px;margin-top:9px">
        <span class="btn-fill" style="width:64px;height:20px;font-size:8px;line-height:20px">Add Plan</span>
        <span class="btn-line" style="width:64px;height:20px;font-size:8px;line-height:18px">Show Detail</span>
      </div>
      <span class="close" style="right:8px;top:8px;width:12px;height:12px"><svg width="12" height="12"><use href="#ico-close"/></svg></span>
    </div>

    <div class="logo-bar" style="left:10px;top:12px;width:246px;height:52px;padding:0 6px 0 10px;gap:9px">
      <span class="logo-mark" style="width:28px;height:28px"></span>
      <span class="logo-name" style="font-size:15px">Lantern Route</span>
      <span class="search-btn" style="width:26px;height:26px"><svg width="14" height="14"><use href="#ico-search"/></svg></span>
    </div>
    <div class="pill red" style="left:273px;top:24px;width:76px;height:28px;font-size:11px">360° ON <span class="dot"></span></div>

    <div class="panel">
      <div class="panel-head">PLANNING<svg width="9" height="6"><path d="M0 0h9L4.5 6z" fill="#fff"/></svg></div>
      <div class="share"><svg width="9" height="9"><use href="#ico-share"/></svg>SHARE</div>
      <div class="scroll"></div>
      <span class="stop-num current" style="top:114px">1</span>
      <div class="stop current" style="top:106px">地蔵寺<br>Jizo Temple<span class="more"></span></div>
      <div class="stop-meta">🚗 2 km &nbsp; ◷ 10 min</div>
      <span class="stop-num" style="top:168px">2</span>
      <div class="stop" style="top:160px">地蔵寺<br>Jizo Temple<span class="more"></span></div>
      <div class="stop-link" style="top:193px"></div>
      <span class="stop-num" style="top:222px">3</span>
      <div class="stop" style="top:214px">地蔵寺<br>Jizo Temple<span class="more"></span></div>
      <div class="stop-link" style="top:247px"></div>
      <span class="stop-num" style="top:276px">4</span>
      <div class="stop" style="top:268px">地蔵寺<br>Jizo Temple<span class="more"></span></div>
      <div class="stop-link" style="top:301px"></div>
      <span class="stop-num" style="top:330px">5</span>
      <div class="stop" style="top:322px">地蔵寺<br>Jizo Temple<span class="more"></span></div>
      <div class="stop-link" style="top:355px"></div>
      <span class="stop-num" style="top:384px">6</span>
      <div class="stop" style="top:376px">地蔵寺<br>Jizo Temple<span class="more"></span></div>
      <div class="optimize">OPTIMIZE ROUTE ORDER</div>
    </div>

    <div class="filter-bar" style="left:273px;top:516px;width:525px;height:48px">
      <div class="filter-select" style="left:5px;top:5px;width:108px;height:38px;font-size:12px">Popular</div>
      <div class="track" style="left:143px;top:23px;width:359px"><span class="range" style="left:211px;width:148px"></span><span class="knob" style="left:204px"></span><span class="knob" style="left:352px"></span></div>
    </div>
    <div class="zoom" style="left:895px;top:502px;width:28px;height:64px;font-size:16px"><span>+</span><span>−</span></div>

    <div class="footer"><b>Lantern Route</b> &nbsp;|&nbsp; Confidential and Proprietary &nbsp;|&nbsp; Terms of Use &nbsp;|&nbsp; External Transmission Policy<span class="code">C45</span></div>
  </div>
</section>

<!-- ============ Row 2 · mobile ============ -->
<section class="frame mobile" style="left:598px;top:433px">
  <div class="screen">
    <div class="map" role="img" aria-label="Terrain map with roads, peaks and place names"></div>
    <svg class="pin" style="left:34px;top:224px"><use href="#pin-dark"/></svg>
    <span class="pin-num" style="left:44px;top:268px">5</span>
    <svg class="pin" style="left:177px;top:224px"><use href="#pin-dark"/></svg>
    <span class="pin-num" style="left:187px;top:268px">4</span>
    <svg class="pin" style="left:104px;top:316px"><use href="#pin-dark"/></svg>
    <span class="pin-num" style="left:114px;top:360px">3</span>
    <svg class="pin" style="left:88px;top:429px"><use href="#pin-dark"/></svg>
    <span class="pin-num" style="left:98px;top:473px">2</span>
    <svg class="pin" style="left:207px;top:376px"><use href="#pin-red"/></svg>
    <span class="pin-num active" style="left:217px;top:420px">1</span>

    <div class="info-card" style="left:194px;top:86px;width:88px;height:58px;padding:5px 6px">
      <h3 style="font-size:11px">XXXXX</h3>
      <p style="font-size:6px;line-height:7px;margin-top:3px;color:var(--ink-soft)">XXXX &nbsp; XXXX<br>XXXX &nbsp; XXXX</p>
      <div style="display:flex;gap:3px;margin-top:4px">
        <span class="btn-fill" style="width:36px;height:10px;font-size:5px;line-height:10px">Add Plan</span>
        <span class="btn-line" style="width:36px;height:10px;font-size:5px;line-height:9px">Show Detail</span>
      </div>
      <span class="close" style="right:4px;top:4px;width:7px;height:7px"><svg width="7" height="7"><use href="#ico-close"/></svg></span>
    </div>

    <div class="pill orange" style="left:14px;top:24px;width:78px;height:27px;font-size:6.5px">OPTIMIZE ROUTE<br>ORDER</div>
    <div class="logo-bar" style="left:109px;top:20px;width:102px;height:32px;padding:0 4px 0 6px;gap:5px">
      <span class="logo-mark" style="width:16px;height:16px"></span>
      <span class="logo-name" style="font-size:8px">Lantern Route</span>
      <span class="search-btn" style="width:16px;height:16px"><svg width="9" height="9"><use href="#ico-search"/></svg></span>
    </div>
    <div class="pill red" style="left:226px;top:25px;width:54px;height:24px;font-size:8px;gap:4px">360° ON <span class="dot" style="width:5px;height:5px"></span></div>

    <div class="zoom" style="left:254px;top:504px;width:20px;height:40px;font-size:11px"><span>+</span><span>−</span></div>
    <div class="filter-bar" style="left:102px;top:544px;width:170px;height:28px">
      <div class="filter-select" style="left:4px;top:4px;width:58px;height:20px;font-size:6px;padding:0 5px">Popular</div>
      <div class="track" style="left:72px;top:13px;width:88px;height:2px"><span class="range" style="left:48px;width:40px;height:2px"></span><span class="knob" style="left:44px;top:-4px;width:9px;height:9px;border-width:2px"></span><span class="knob" style="left:82px;top:-4px;width:9px;height:9px;border-width:2px"></span></div>
    </div>
    <div class="footer"><b>Lantern Route</b> &nbsp;|&nbsp; Confidential and Proprietary &nbsp;|&nbsp; Terms of Use &nbsp;|<br>External Transmission Policy</div>
  </div>
</section>

<!-- ============ Row 3 · desktop: region picker ============ -->
<section class="frame desktop" style="left:62px;top:810px">
  <div class="screen">
    <div class="map" role="img" aria-label="Terrain map with roads, peaks and place names"></div>
    <svg class="pin" style="left:456px;top:29px"><use href="#pin-dark"/></svg>
    <svg class="pin" style="left:736px;top:54px"><use href="#pin-dark"/></svg>
    <svg class="pin" style="left:835px;top:184px"><use href="#pin-dark"/></svg>
    <svg class="pin" style="left:803px;top:347px"><use href="#pin-dark"/></svg>
    <svg class="pin" style="left:813px;top:484px"><use href="#pin-dark"/></svg>

    <div class="logo-bar" style="left:10px;top:12px;width:246px;height:52px;padding:0 6px 0 10px;gap:9px">
      <span class="logo-mark" style="width:28px;height:28px"></span>
      <span class="logo-name" style="font-size:15px">Lantern Route</span>
      <span class="search-btn" style="width:26px;height:26px"><svg width="14" height="14"><use href="#ico-search"/></svg></span>
    </div>
    <div class="pill red" style="left:273px;top:24px;width:76px;height:28px;font-size:11px">360° ON <span class="dot"></span></div>
    <div class="panel">
      <div class="panel-head">PLANNING<svg width="9" height="6"><path d="M0 0h9L4.5 6z" fill="#fff"/></svg></div>
      <div class="share"><svg width="9" height="9"><use href="#ico-share"/></svg>SHARE</div>
      <span class="stop-num current" style="top:114px">1</span>
      <div class="stop current" style="top:106px">地蔵寺<br>Jizo Temple</div>
      <div class="stop-meta">🚗 2 km &nbsp; ◷ 10 min</div>
      <span class="stop-num" style="top:168px">2</span>
      <div class="stop" style="top:160px">地蔵寺<br>Jizo Temple</div>
      <span class="stop-num" style="top:222px">3</span>
      <div class="stop" style="top:214px">地蔵寺<br>Jizo Temple</div>
      <span class="stop-num" style="top:276px">4</span>
      <div class="stop" style="top:268px">地蔵寺<br>Jizo Temple</div>
      <span class="stop-num" style="top:330px">5</span>
      <div class="stop" style="top:322px">地蔵寺<br>Jizo Temple</div>
      <span class="stop-num" style="top:384px">6</span>
      <div class="stop" style="top:376px">地蔵寺<br>Jizo Temple</div>
      <div class="optimize">OPTIMIZE ROUTE ORDER</div>
    </div>
    <div class="filter-bar" style="left:273px;top:516px;width:525px;height:48px">
      <div class="filter-select" style="left:5px;top:5px;width:108px;height:38px;font-size:12px">Popular</div>
      <div class="track" style="left:143px;top:23px;width:359px"><span class="range" style="left:211px;width:148px"></span><span class="knob" style="left:204px"></span><span class="knob" style="left:352px"></span></div>
    </div>
    <div class="zoom" style="left:895px;top:502px;width:28px;height:64px;font-size:16px"><span>+</span><span>−</span></div>
    <div class="footer"><b>Lantern Route</b> &nbsp;|&nbsp; Confidential and Proprietary &nbsp;|&nbsp; Terms of Use &nbsp;|&nbsp; External Transmission Policy<span class="code">C45</span></div>
    <div class="dim"></div>

    <div class="modal" style="left:230px;top:102px;width:481px;height:428px">
      <span class="close" style="right:9px;top:9px;width:14px;height:14px"><svg width="14" height="14"><use href="#ico-close"/></svg></span>
      <h2 class="modal-title" style="font-size:40px;margin-top:22px">Map of <em>Japan</em></h2>
      <div class="japan" role="img" aria-label="Outline map of Japan divided into prefectures" style="left:61px;top:93px;width:342px;height:175px"></div>
      <span class="region" style="left:336px;top:102px;font-size:9px;line-height:18px">HOKKAIDO</span>
      <span class="region" style="left:110px;top:190px;font-size:9px;line-height:18px">FUKUOKA</span>
      <span class="region" style="left:198px;top:190px;font-size:9px;line-height:18px">KYOTO</span>
      <span class="region" style="left:198px;top:214px;font-size:9px;line-height:18px">OSAKA</span>
      <span class="region hub" style="left:324px;top:214px;font-size:9px;line-height:18px">TOKYO</span>
      <span class="region" style="left:61px;top:237px;font-size:9px;line-height:18px">OKINAWA</span>
      <span class="region" style="left:271px;top:242px;font-size:9px;line-height:18px">NAGOYA</span>
      <hr style="left:21px;top:303px;width:438px">
      <div class="airports" style="top:337px;gap:11px">
        <div class="airport-row" style="gap:6px">
          <span class="airport" style="height:23px;padding-right:12px;gap:8px;font-size:8.5px"><i style="width:20px;height:20px"><svg width="10" height="10"><use href="#ico-plane"/></svg></i>NARITA</span>
          <span class="airport" style="height:23px;padding-right:12px;gap:8px;font-size:8.5px"><i style="width:20px;height:20px"><svg width="10" height="10"><use href="#ico-plane"/></svg></i>KANSAI</span>
          <span class="airport" style="height:23px;padding-right:12px;gap:8px;font-size:8.5px"><i style="width:20px;height:20px"><svg width="10" height="10"><use href="#ico-plane"/></svg></i>HANEDA</span>
          <span class="airport" style="height:23px;padding-right:12px;gap:8px;font-size:8.5px"><i style="width:20px;height:20px"><svg width="10" height="10"><use href="#ico-plane"/></svg></i>FUKUOKA</span>
          <span class="airport" style="height:23px;padding-right:12px;gap:8px;font-size:8.5px"><i style="width:20px;height:20px"><svg width="10" height="10"><use href="#ico-plane"/></svg></i>CHUBU</span>
        </div>
        <div class="airport-row" style="gap:6px">
          <span class="airport" style="height:23px;padding-right:12px;gap:8px;font-size:8.5px"><i style="width:20px;height:20px"><svg width="10" height="10"><use href="#ico-plane"/></svg></i>SHIN-CHITOSE</span>
          <span class="airport" style="height:23px;padding-right:12px;gap:8px;font-size:8.5px"><i style="width:20px;height:20px"><svg width="10" height="10"><use href="#ico-plane"/></svg></i>NAHA</span>
          <span class="airport" style="height:23px;padding-right:12px;gap:8px;font-size:8.5px"><i style="width:20px;height:20px"><svg width="10" height="10"><use href="#ico-plane"/></svg></i>TAKAMATSU</span>
          <span class="airport" style="height:23px;padding-right:12px;gap:8px;font-size:8.5px"><i style="width:20px;height:20px"><svg width="10" height="10"><use href="#ico-plane"/></svg></i>SENDAI</span>
          <span class="airport" style="height:23px;padding-right:12px;gap:8px;font-size:8.5px"><i style="width:20px;height:20px"><svg width="10" height="10"><use href="#ico-plane"/></svg></i>MIYAZAKI</span>
        </div>
      </div>
    </div>
  </div>
</section>

<!-- ============ Row 3 · mobile ============ -->
<section class="frame mobile" style="left:598px;top:810px">
  <div class="screen">
    <div class="map" role="img" aria-label="Terrain map with roads, peaks and place names"></div>
    <div class="pill orange" style="left:14px;top:24px;width:78px;height:27px;font-size:6.5px">OPTIMIZE ROUTE<br>ORDER</div>
    <div class="logo-bar" style="left:109px;top:20px;width:102px;height:32px;padding:0 4px 0 6px;gap:5px">
      <span class="logo-mark" style="width:16px;height:16px"></span>
      <span class="logo-name" style="font-size:8px">Lantern Route</span>
      <span class="search-btn" style="width:16px;height:16px"><svg width="9" height="9"><use href="#ico-search"/></svg></span>
    </div>
    <div class="pill red" style="left:226px;top:25px;width:54px;height:24px;font-size:8px;gap:4px">360° ON <span class="dot" style="width:5px;height:5px"></span></div>
    <div class="filter-bar" style="left:26px;top:544px;width:240px;height:28px">
      <div class="filter-select" style="left:4px;top:4px;width:68px;height:20px;font-size:7px;padding:0 6px">Popular</div>
    </div>
    <div class="footer"><b>Lantern Route</b> &nbsp;|&nbsp; Confidential and Proprietary &nbsp;|&nbsp; Terms of Use &nbsp;|<br>External Transmission Policy</div>
    <div class="dim"></div>

    <div class="modal" style="left:16px;top:128px;width:261px;height:375px;border-radius:12px">
      <span class="close" style="right:9px;top:9px;width:11px;height:11px"><svg width="11" height="11"><use href="#ico-close"/></svg></span>
      <h2 class="modal-title" style="font-size:22px;margin-top:22px">Map of <em>Japan</em></h2>
      <div class="japan" role="img" aria-label="Outline map of Japan divided into prefectures" style="left:8px;top:72px;width:245px;height:150px"></div>
      <span class="region" style="left:202px;top:83px;font-size:5px;line-height:10px;padding:0 5px">HOKKAIDO</span>
      <span class="region" style="left:24px;top:157px;font-size:5px;line-height:10px;padding:0 5px">FUKUOKA</span>
      <span class="region" style="left:110px;top:157px;font-size:5px;line-height:10px;padding:0 5px">KYOTO</span>
      <span class="region" style="left:110px;top:174px;font-size:5px;line-height:10px;padding:0 5px">OSAKA</span>
      <span class="region hub" style="left:205px;top:180px;font-size:5px;line-height:10px;padding:0 5px">TOKYO</span>
      <span class="region" style="left:6px;top:195px;font-size:5px;line-height:10px;padding:0 5px">OKINAWA</span>
      <span class="region" style="left:158px;top:196px;font-size:5px;line-height:10px;padding:0 5px">NAGOYA</span>
      <hr style="left:21px;top:245px;width:219px">
      <div class="airports" style="top:270px;gap:6px">
        <div class="airport-row" style="gap:4px">
          <span class="airport" style="height:15px;padding-right:7px;gap:5px;font-size:5px"><i style="width:12px;height:12px"><svg width="7" height="7"><use href="#ico-plane"/></svg></i>NARITA</span>
          <span class="airport" style="height:15px;padding-right:7px;gap:5px;font-size:5px"><i style="width:12px;height:12px"><svg width="7" height="7"><use href="#ico-plane"/></svg></i>KANSAI</span>
          <span class="airport" style="height:15px;padding-right:7px;gap:5px;font-size:5px"><i style="width:12px;height:12px"><svg width="7" height="7"><use href="#ico-plane"/></svg></i>HANEDA</span>
          <span class="airport" style="height:15px;padding-right:7px;gap:5px;font-size:5px"><i style="width:12px;height:12px"><svg width="7" height="7"><use href="#ico-plane"/></svg></i>FUKUOKA</span>
        </div>
        <div class="airport-row" style="gap:4px">
          <span class="airport" style="height:15px;padding-right:7px;gap:5px;font-size:5px"><i style="width:12px;height:12px"><svg width="7" height="7"><use href="#ico-plane"/></svg></i>CHUBU</span>
          <span class="airport" style="height:15px;padding-right:7px;gap:5px;font-size:5px"><i style="width:12px;height:12px"><svg width="7" height="7"><use href="#ico-plane"/></svg></i>SHIN-CHITOSE</span>
          <span class="airport" style="height:15px;padding-right:7px;gap:5px;font-size:5px"><i style="width:12px;height:12px"><svg width="7" height="7"><use href="#ico-plane"/></svg></i>NAHA</span>
        </div>
        <div class="airport-row" style="gap:4px">
          <span class="airport" style="height:15px;padding-right:7px;gap:5px;font-size:5px"><i style="width:12px;height:12px"><svg width="7" height="7"><use href="#ico-plane"/></svg></i>TAKAMATSU</span>
          <span class="airport" style="height:15px;padding-right:7px;gap:5px;font-size:5px"><i style="width:12px;height:12px"><svg width="7" height="7"><use href="#ico-plane"/></svg></i>SENDAI</span>
          <span class="airport" style="height:15px;padding-right:7px;gap:5px;font-size:5px"><i style="width:12px;height:12px"><svg width="7" height="7"><use href="#ico-plane"/></svg></i>MIYAZAKI</span>
        </div>
      </div>
    </div>
  </div>
</section>

</body>
</html>
```